Solace Chiropractic & Acupuncture Business Cards

I need a business card design that feels elevated. I am open to any of the logo designs uploaded. We have two doctors so I'll need to be able to change out the names.

Information:
Marnie Toller D.C., Dipl. Ac. ASA
584 W 12th St, Ste 320
Hutchinson, KS 67419
solacegrove.net
620-555-0147
drmarnie@solacegrove.com
Updates

We have designs we like now, we are just trying to choose between top contenders. Thanks for your submissions!

Contact Information for Business Card

noted in description

Requirements
Must have
• ability to edit info if possible
Nice to have
• Please see our website solacegrove.net for our style and colors

```html
<!DOCTYPE html>
<html lang="en">
<head>
<meta charset="utf-8">
<title>Solace Chiropractic &amp; Acupuncture – Business Cards</title>
<link rel="stylesheet" href="https://fonts.googleapis.com/css2?family=Crimson+Text:wght@400;600&display=swap">
<style>
  :root {
    --navy: #2e3b55;
    --ink: #2a3752;
    --ink-soft: #4a5570;
    --paper: #fbfbf8;
    --stage: #e4e4e2;
  }
  * { margin: 0; padding: 0; box-sizing: border-box; }
  html, body { width: 1200px; height: 900px; overflow: hidden; }
  body {
    background: var(--stage);
    font-family: "Crimson Text", Georgia, serif;
    display: flex;
    flex-direction: column;
    align-items: center;
    justify-content: center;
    gap: 44px;
  }
  .card {
    width: 600px;
    height: 343px;
    position: relative;
    box-shadow: 0 6px 18px rgba(0,0,0,0.18);
  }

  /* Back of card */
  .card-back {
    background: var(--navy);
    color: var(--paper);
    display: flex;
    flex-direction: column;
    align-items: center;
    justify-content: center;
  }
  .card-back .name { font-size: 40px; font-weight: 400; letter-spacing: 0.5px; line-height: 1; }
  .card-back .role { font-size: 17px; margin-top: 6px; }

  /* Front of card */
  .card-front { background: var(--paper); color: var(--ink); }
  .card-front .name {
    position: absolute; left: 44px; top: 38px;
    font-size: 28px; font-weight: 600; line-height: 1;
  }
  .card-front .credentials {
    position: absolute; left: 46px; top: 72px;
    font-size: 13px; color: var(--ink-soft);
  }
  .contact-labels {
    position: absolute; left: 62px; top: 128px;
    list-style: none; font-size: 14px; line-height: 22px; color: var(--ink-soft);
  }
  .contact-divider {
    position: absolute; left: 178px; top: 150px;
    width: 1px; height: 96px; background: var(--ink);
  }
  .contact-values {
    position: absolute; left: 200px; top: 176px;
    list-style: none; font-size: 16px; line-height: 25px; color: var(--ink);
  }
  .practice-mark {
    position: absolute; right: 38px; top: 130px;
    width: 130px; text-align: center;
    font-size: 15px; line-height: 1.15; color: var(--ink);
    text-transform: uppercase; letter-spacing: 1.5px;
  }
  .practice-mark .mark-square {
    display: block; width: 14px; height: 14px; margin: 0 auto 10px;
    background: var(--navy);
  }
</style>
</head>
<body>
  <section class="card card-back">
    <h1 class="name">Marnie Toller</h1>
    <p class="role">Doctor</p>
  </section>

  <section class="card card-front">
    <h2 class="name">Marnie Toller</h2>
    <p class="credentials">D.C., Dipl. Ac. ASA</p>

    <ul class="contact-labels">
      <li>Phone</li>
      <li>Web</li>
      <li>Email</li>
      <li>Address</li>
    </ul>
    <div class="contact-divider"></div>
    <ul class="contact-values">
      <li>620-555-0147</li>
      <li>solacegrove.net</li>
      <li>drmarnie@solacegrove.com</li>
      <li>584 W 12th St, Ste 320, Hutchinson, KS 67419</li>
    </ul>

    <div class="practice-mark">
      <span class="mark-square"></span>
      Solace Chiropractic &amp; Acupuncture
    </div>
  </section>
</body>
</html>
```